Design my New and Engaging Wix Website

We just recently started a new website for peace education (www.harmony-learning.example) and would like to have a custom design for it. The design should be engaging and modern. You can use our logo and design the website inspired by the style.

```html
<!DOCTYPE html>
<html lang="en">
<head>
<meta charset="utf-8">
<title>Harmony Learning – Home Page Concepts</title>
<link href="https://fonts.googleapis.com/css2?family=Poppins:wght@400;500;600;700;800&display=swap" rel="stylesheet">
<style>
:root{
  --board:#a7a7a7;
  --blue:#1a8fe3;
  --sky:#1296f0;
  --navy:#1b1f6b;
  --deep:#161a5e;
  --ink:#2a2a2a;
  --muted:#6b6b6b;
  --pale:#eef6fb;
  --mist:#ededed;
  --white:#ffffff;
  --black:#050505;
}
*{box-sizing:border-box;margin:0;padding:0}
html,body{width:1200px;height:2459px;overflow:hidden}
body{background:var(--board);font-family:"Poppins",sans-serif;color:var(--ink);position:relative}
.board-label{position:absolute;top:42px;width:300px;text-align:center;color:var(--white);font-weight:800;font-size:24px;letter-spacing:.3px}
.page{position:absolute;top:118px;width:426px;background:var(--white);overflow:hidden}
.page-one{left:92px;height:2262px}
.page-two{left:658px;height:2078px}
.abs{position:absolute}
.art{position:absolute;border-radius:4px}

/* navigation */
.nav{position:absolute;left:0;top:0;width:426px;height:39px;background:var(--white)}
.brand{position:absolute;left:50px;top:13px;display:flex;align-items:center;gap:5px;color:var(--blue);font-weight:600;font-size:10px;white-space:nowrap}
.brand-dot{width:9px;height:9px;border-radius:50%;background:var(--blue)}
.nav-links{position:absolute;left:173px;top:16px;display:flex;font-size:6.5px;color:var(--ink)}
.nav-links span{margin-right:17px}
.nav-links .active{color:var(--blue)}

/* hero */
.hero{position:absolute;left:0;top:39px;width:426px;height:272px;background:linear-gradient(180deg,#45a4ee 0%,#7c8fe6 30%,#b59ae0 48%,#3b3aa6 62%,#1e1f78 100%)}
.hero-wave{position:absolute;left:0;top:200px;width:426px;height:111px}
.hero-title{position:absolute;left:210px;top:92px;width:205px;font-size:14.5px;line-height:21px;font-weight:600;color:var(--deep)}
.btn{position:absolute;background:var(--blue);color:var(--white);border-radius:14px;font-size:7px;font-weight:600;display:flex;align-items:center;justify-content:center}
.hero-btn{left:210px;top:159px;width:81px;height:23px}

.h-section{position:absolute;font-weight:700;color:var(--blue);font-size:16px;line-height:1}
.center{left:0;width:426px;text-align:center}
.copy{position:absolute;font-size:4.8px;line-height:7.6px;color:var(--ink)}

/* what we do cards */
.wwd-band{position:absolute;left:0;top:730px;width:426px;height:326px;background:var(--pale)}
.card{position:absolute;top:806px;width:113px;height:188px;background:var(--white);text-align:center}
.card .art{left:14px;top:18px;width:85px;height:58px}
.card-title{position:absolute;left:8px;width:97px;font-size:6.5px;line-height:8.5px;font-weight:600;color:var(--blue)}
.card-text{position:absolute;left:10px;width:93px;font-size:6px;line-height:8.5px;color:var(--ink)}

/* classes */
.classes{position:absolute;left:0;top:1056px;width:426px;height:274px;background:var(--sky)}
.classes-copy{position:absolute;left:66px;width:294px;text-align:center;color:var(--white);font-size:5.8px;line-height:9.8px}
.play{position:absolute;border:2px solid var(--white);border-radius:50%}
.play svg{position:absolute;inset:0;margin:auto}

/* testimonials */
.story{position:absolute;top:1536px;width:141px;height:195px;background:#f4f5f7;overflow:hidden}
.quote-mark{position:absolute;left:0;width:141px;text-align:center;font-size:22px;font-weight:800;color:var(--ink);line-height:1}
.quote-text{position:absolute;left:16px;width:110px;text-align:center;font-size:4.8px;line-height:6.6px;font-style:italic;color:var(--ink)}
.quote-name{position:absolute;font-size:5.5px;color:var(--ink);display:flex;align-items:center;gap:5px}
.quote-name::before{content:"";width:14px;height:1px;background:var(--ink)}
.arrow{position:absolute;width:20px;height:20px;border-radius:50%;background:var(--blue)}

/* forms */
.field{position:absolute;background:var(--white);font-size:4.8px;color:var(--ink);padding:3px 4px;border:1px solid #d8dbe6}

/* footer page one */
.footer-dark{position:absolute;left:0;top:2030px;width:426px;height:232px;background:var(--black);color:var(--white)}
.foot-head{position:absolute;font-size:7px;font-weight:500;color:var(--white)}
.foot-list{position:absolute;font-size:5.5px;line-height:13px;list-style:none;color:var(--white)}
.foot-list li::before{content:"";display:inline-block;width:4px;height:4px;border-radius:50%;background:var(--white);margin-right:4px;vertical-align:middle}
.foot-small{position:absolute;font-size:4.6px;line-height:6.6px;font-weight:600;color:var(--white)}

/* page two rows */
.row-title{position:absolute;font-size:8.8px;line-height:11px;font-weight:600;color:var(--blue)}
.row-sub{position:absolute;font-size:6.5px;line-height:9px;font-weight:500;color:var(--ink)}
.row-copy{position:absolute;font-size:6.2px;line-height:9.6px;color:var(--muted)}
.about{position:absolute;left:0;top:927px;width:426px;height:248px;background:linear-gradient(180deg,#128de8,#1aa0f3)}
.about-copy{position:absolute;left:50px;top:1006px;width:144px;font-size:5.2px;line-height:9.6px;color:var(--white)}
.blog-band{position:absolute;left:0;top:1416px;width:426px;height:320px;background:var(--mist)}
.blog-title{position:absolute;font-size:6.3px;line-height:8px;font-weight:500;color:var(--ink)}
.blog-date{position:absolute;font-size:4.4px;color:var(--blue)}
.blog-copy{position:absolute;font-size:4.6px;line-height:6.4px;color:var(--muted)}
.contact-navy{position:absolute;left:0;top:1746px;width:426px;height:225px;background:linear-gradient(180deg,#1b1f6b,#1c2a86 70%,#1b2073)}
.contact-item{position:absolute;display:flex;align-items:center;gap:5px;color:var(--white);font-size:6px}
.icon-round{width:19px;height:19px;border-radius:50%;background:var(--blue);display:flex;align-items:center;justify-content:center}
.footer-light{position:absolute;left:0;top:1971px;width:426px;height:107px;background:#e6eef6;text-align:center}
.footer-light .line{position:absolute;left:0;width:426px;font-size:5.2px;line-height:7px;color:var(--ink)}
</style>
</head>
<body>

<div class="board-label" style="left:121px">HOME PAGE 1</div>
<div class="board-label" style="left:727px">HOME PAGE 2</div>

<!-- ================= HOME PAGE 1 ================= -->
<section class="page page-one">
  <header class="nav">
    <div class="brand"><span class="brand-dot"></span>Harmony Learning</div>
    <nav class="nav-links"><span class="active">Home</span><span>About Us</span><span>Courses</span><span>Blog</span><span>Testimonial</span></nav>
  </header>

  <div class="hero" role="img" aria-label="Illustration of a person with a laptop sitting on a hillside above a misty lake at dusk"></div>
  <svg class="hero-wave" viewBox="0 0 426 111" preserveAspectRatio="none">
    <path d="M0,59 C90,56 200,104 290,108 C350,110 400,86 426,62 V111 H0 Z" fill="#ffffff"/>
    <path d="M190,90 C230,102 260,107 290,108 C350,110 400,86 426,62" fill="none" stroke="#1a8fe3" stroke-width="4"/>
  </svg>
  <h1 class="hero-title">QUALITATIVE AND ACCESSIBLE PEACE EDUCATION RESOURCES</h1>
  <div class="btn hero-btn">GET TO KNOW</div>

  <!-- mission -->
  <div class="art" style="left:52px;top:350px;width:152px;height:109px;background:linear-gradient(135deg,#dbe9fb,#9cc6f3 60%,#f2c9a0)" role="img" aria-label="Illustration of an online class with a teacher on a large screen and students studying"></div>
  <h2 class="h-section" style="left:227px;top:351px">OUR MISSION</h2>
  <p class="copy" style="left:227px;top:373px;width:136px">In an increasingly internationalized world, complex and manifold conflicts arise between individuals, groups, organizations, and states. To find ways of dealing with these issues in a constructive and peaceful manner is a central challenge for modern societies.</p>
  <p class="copy" style="left:227px;top:420px;width:136px;color:#555">Harmony Learning aims to empower communities affected by unresolved conflicts and strengthen their capacities to address them effectively.</p>
  <div class="btn" style="left:231px;top:455px;width:81px;height:25px">READ MORE</div>

  <!-- contribution -->
  <h2 class="h-section" style="left:61px;top:523px">CONTRIBUTION</h2>
  <p class="copy" style="left:61px;top:548px;width:135px">In an increasingly internationalized world, complex and manifold conflicts arise between individuals, groups, organizations, and states. To find ways of dealing with these issues in a constructive and peaceful manner is a central challenge for modern societies.</p>
  <p class="copy" style="left:61px;top:593px;width:135px">Harmony Learning aims to empower communities affected by unresolved conflicts and strengthen their capacities to address them effectively.</p>
  <div class="btn" style="left:62px;top:628px;width:82px;height:25px">READ MORE</div>
  <div class="art" style="left:200px;top:517px;width:191px;height:129px;background:linear-gradient(135deg,#e4eefb,#7fb0ef 55%,#3c4bb0)" role="img" aria-label="Illustration of two people working at desks in front of a large screen dashboard"></div>

  <!-- what we do -->
  <div class="wwd-band"></div>
  <svg class="abs" style="left:0;top:690px" width="426" height="70" viewBox="0 0 426 70">
    <path d="M0,70 V58 C60,40 120,6 200,6 C280,8 350,46 426,55 V70 Z" fill="#eef6fb"/>
    <path d="M30,42 C90,14 150,4 210,6 C290,10 350,44 426,55" fill="none" stroke="#1a8fe3" stroke-width="5"/>
    <rect x="0" y="56" width="426" height="14" fill="#eef6fb"/>
  </svg>
  <h2 class="h-section center" style="top:762px">WHAT WE DO</h2>

  <div class="card" style="left:34px">
    <div class="art" style="background:linear-gradient(135deg,#e7effa,#6aa8ee 60%,#2a3a9a)" role="img" aria-label="Illustration of students studying beside stacked books and a graduation cap"></div>
    <div class="card-title" style="top:104px">DEVELOPING<br>PEACE EDUCATION<br>CURRICULAR</div>
    <div class="card-text" style="top:140px">Modernizing and internationalizing higher education</div>
  </div>
  <div class="card" style="left:157px">
    <div class="art" style="background:linear-gradient(135deg,#eef1f6,#b9c4d6 55%,#2a7fe0)" role="img" aria-label="Illustration of a woman working on a laptop with bookshelves and a video icon"></div>
    <div class="card-title" style="top:90px">TEACHING AND<br>TRAINING</div>
    <div class="card-text" style="top:124px">Utilizing the potential of hybrid learning</div>
  </div>
  <div class="card" style="left:283px">
    <div class="art" style="background:linear-gradient(135deg,#eef4fb,#8fbbef 55%,#2e3b86)" role="img" aria-label="Illustration of a presenter at a whiteboard and a person with a laptop"></div>
    <div class="card-title" style="top:90px">PRODUCING<br>PEACE EDUCATION<br>RESOURCES</div>
    <div class="card-text" style="top:128px">Modernizing and internationalizing higher education</div>
  </div>

  <!-- classes -->
  <div class="classes"></div>
  <h2 class="h-section center" style="top:1101px;color:#fff">CLASSES</h2>
  <p class="classes-copy" style="top:1134px">Within our pilot project "Open Pathways for Peace Learning" the Northbridge University (NBU) in cooperation with the Eastvale National Academy (ENA) uses means of digitalization to develop and teach up-to-date skills in conflict analysis and conflict transformation. These efforts are supported by the Academic Exchange Council (AEC) within the program "Bridges for Learning: partner university exchange grants".</p>
  <p class="classes-copy" style="top:1208px">Within our pilot project "Open Pathways for Peace Learning" the Northbridge University</p>
  <div class="art" style="left:42px;top:1266px;width:341px;height:189px;border-radius:0;background:linear-gradient(180deg,#5fa9ef 0%,#9fb8ee 35%,#6e74d2 60%,#23246e 100%)" role="img" aria-label="Video still: a person relaxing in a deck chair with a laptop on a forested hilltop"></div>
  <div class="play" style="left:60px;top:1413px;width:30px;height:30px"><svg width="12" height="14" viewBox="0 0 12 14"><path d="M2,1 L11,7 L2,13 Z" fill="#fff"/></svg></div>

  <!-- success stories -->
  <h2 class="h-section center" style="top:1492px">SUCESS STORIES</h2>
  <div class="story" style="left:61px">
    <div class="art" style="left:0;top:0;width:141px;height:104px;border-radius:0;background:linear-gradient(135deg,#d9c2a8,#b6c6d9 60%,#dfe7f0)" role="img" aria-label="Portrait photo of a smiling woman in a light blazer"></div>
    <svg class="abs" style="left:0;top:70px" width="141" height="40" viewBox="0 0 141 40">
      <path d="M0,28 C40,40 100,40 141,0 V40 H0 Z" fill="#f4f5f7"/>
      <path d="M0,28 C40,40 100,40 141,0" fill="none" stroke="#7cc0f2" stroke-width="4"/>
    </svg>
    <div class="quote-mark" style="top:116px">&ldquo;</div>
    <p class="quote-text" style="top:139px">Lorem Ipsum is simply dummy text of the printing and typesetting industry. Lorem Ipsum has been the industry's standard dummy text ever since the 1500s, when an unknown printer</p>
    <div class="quote-name" style="left:68px;top:175px">NORA VALE</div>
  </div>
  <div class="story" style="left:225px">
    <div class="quote-mark" style="top:10px">&ldquo;</div>
    <p class="quote-text" style="top:33px">Lorem Ipsum is simply dummy text of the printing and typesetting industry. Lorem Ipsum has been the industry's standard dummy text ever since the 1500s, when an unknown printer</p>
    <div class="quote-name" style="left:72px;top:72px">DANIEL</div>
    <div class="art" style="left:0;top:100px;width:141px;height:95px;border-radius:0;background:linear-gradient(135deg,#c9d4e2,#e7d2bd 55%,#6e8fb8)" role="img" aria-label="Portrait photo of a smiling man in a light blue shirt"></div>
    <svg class="abs" style="left:0;top:92px" width="141" height="40" viewBox="0 0 141 40">
      <path d="M0,40 C30,0 90,2 141,14 V0 H0 Z" fill="#f4f5f7"/>
      <path d="M0,40 C30,0 90,2 141,14" fill="none" stroke="#7cc0f2" stroke-width="4"/>
    </svg>
  </div>
  <div class="arrow" style="left:23px;top:1622px"><svg width="20" height="20" viewBox="0 0 20 20"><path d="M12,6 L8,10 L12,14" fill="none" stroke="#fff" stroke-width="1.6"/></svg></div>
  <div class="arrow" style="left:382px;top:1622px"><svg width="20" height="20" viewBox="0 0 20 20"><path d="M8,6 L12,10 L8,14" fill="none" stroke="#fff" stroke-width="1.6"/></svg></div>

  <!-- contact -->
  <div class="art" style="left:0;top:1795px;width:426px;height:250px;border-radius:0;background:linear-gradient(180deg,#1f8fe6 0%,#4a7fe0 40%,#3340b0 70%,#1e237a 100%)" role="img" aria-label="Illustration of a woman with a phone and laptop sitting on a hillside with mountains"></div>
  <h2 class="h-section" style="left:240px;top:1836px;color:#fff">CONTACT US</h2>
  <div class="field" style="left:225px;top:1862px;width:152px;height:15px">Your Name</div>
  <div class="field" style="left:225px;top:1881px;width:152px;height:15px">Email Address</div>
  <div class="field" style="left:225px;top:1900px;width:152px;height:15px">Phone</div>
  <div class="field" style="left:225px;top:1919px;width:152px;height:68px">Message</div>
  <div class="btn" style="left:269px;top:1978px;width:65px;height:18px">SUBMIT</div>
  <svg class="abs" style="left:0;top:1996px" width="426" height="36" viewBox="0 0 426 36">
    <path d="M0,36 V33 C100,12 250,6 426,14 V36 Z" fill="#050505"/>
    <path d="M0,33 C100,12 250,6 426,14" fill="none" stroke="#1a8fe3" stroke-width="4"/>
  </svg>

  <footer class="footer-dark">
    <div class="abs" style="left:0;top:29px;width:426px;text-align:center;font-size:6.5px">SUBSCRIBE TODAY!</div>
    <div class="abs" style="left:126px;top:51px;width:94px;height:18px;background:#fff;border-radius:9px;color:#222;font-size:5.5px;padding:5px 10px">Email Address</div>
    <div class="btn" style="left:228px;top:50px;width:56px;height:18px">SIGN UP</div>
    <div class="brand" style="left:66px;top:84px"><span class="brand-dot"></span>Harmony Learning</div>
    <div class="foot-small" style="left:61px;top:129px;width:110px">Cross-Border Cooperation</div>
    <div class="foot-small" style="left:61px;top:142px;width:110px">NORTHBRIDGE UNIVERSITY</div>
    <div class="foot-small" style="left:61px;top:155px;width:110px">EASTVALE NATIONAL ACADEMY</div>
    <div class="foot-head" style="left:178px;top:98px">Explore</div>
    <ul class="foot-list" style="left:178px;top:112px"><li>Home</li><li>About Us</li><li>Courses</li><li>Blog</li><li>Testimonial</li></ul>
    <div class="foot-head" style="left:239px;top:98px">Visit</div>
    <div class="abs" style="left:239px;top:113px;width:72px;font-size:5.5px;line-height:7.2px">
      <svg width="5" height="6" viewBox="0 0 10 12" style="vertical-align:middle"><path d="M5,0 C2,0 0,2 0,5 C0,8 5,12 5,12 C5,12 10,8 10,5 C10,2 8,0 5,0 Z" fill="#fff"/></svg> Lorem ipsum dolo adipiscing elitelusmod tempor didunt ut labore et
    </div>
    <div class="abs" style="left:239px;top:163px;font-size:5.5px">&#9742;(555) 010 3377</div>
    <div class="foot-head" style="left:325px;top:98px">DONOR</div>
    <div class="abs" style="left:325px;top:115px;width:43px;height:16px;background:#fff"></div>
    <div class="foot-small" style="left:325px;top:136px;width:50px;font-size:4px;line-height:5.4px">ACADEMIC EXCHANGE COUNCIL</div>
    <div class="abs" style="left:0;top:196px;width:426px;height:1px;background:#3a3a3a"></div>
    <div class="abs" style="left:0;top:213px;width:426px;text-align:center;font-size:5.5px">© 2021All Rights Reserved. Privacy Policy &nbsp;|&nbsp; Sitemap</div>
  </footer>
</section>

<!-- ================= HOME PAGE 2 ================= -->
<section class="page page-two">
  <header class="nav">
    <div class="brand"><span class="brand-dot"></span>Harmony Learning</div>
    <nav class="nav-links"><span class="active">Home</span><span>About Us</span><span>Courses</span><span>Blog</span><span>Testimonial</span></nav>
  </header>

  <div class="hero" role="img" aria-label="Illustration of a person with a laptop sitting on a hillside above a misty lake at dusk"></div>
  <svg class="hero-wave" viewBox="0 0 426 111" preserveAspectRatio="none">
    <path d="M0,59 C90,56 200,104 290,108 C350,110 400,86 426,62 V111 H0 Z" fill="#ffffff"/>
    <path d="M190,90 C230,102 260,107 290,108 C350,110 400,86 426,62" fill="none" stroke="#1a8fe3" stroke-width="4"/>
  </svg>
  <h1 class="hero-title">QUALITATIVE AND ACCESSIBLE PEACE EDUCATION RESOURCES</h1>
  <div class="btn hero-btn">GET TO KNOW</div>

  <h2 class="h-section center" style="top:342px;font-size:17px">WHAT WE DO</h2>

  <div class="row-title" style="left:61px;top:401px;width:128px">DEVELOPING PEACE EDUCATION CURRICULAR</div>
  <div class="row-sub" style="left:61px;top:432px;width:120px">Modernizing and internationalizing higher education</div>
  <p class="row-copy" style="left:61px;top:457px;width:130px">Lorem ipsum dolor sit amet, consectetur adipiscing elit, sed do eiusmod tempor incididunt ut labore et dolore magna aliqu auis ipsum suspendisse ultrices gravida. Risus commodo viverra maecenas acc umsan lacus vel facilisis.</p>
  <div class="art" style="left:206px;top:388px;width:181px;height:119px;background:linear-gradient(135deg,#eef2f8,#7eb3ef 55%,#2a3a9a)" role="img" aria-label="Illustration of students studying beside stacked books, a screen and a graduation cap"></div>

  <div class="art" style="left:23px;top:564px;width:197px;height:124px;background:linear-gradient(135deg,#f1f2f5,#c7ccd6 55%,#2b84e2)" role="img" aria-label="Illustration of a woman working on a laptop with bookshelves and a video icon"></div>
  <div class="row-title" style="left:240px;top:574px;width:128px">PRODUCING PEACE EDUCATION RESOURCES</div>
  <div class="row-sub" style="left:240px;top:605px;width:110px">Providing engaging and high quality content</div>
  <p class="row-copy" style="left:240px;top:631px;width:130px">Lorem ipsum dolor sit amet, consectetur adipiscing elit, sed do eiusmod tempor incididunt ut labore et dolore magna aliqu auis ipsum suspendisse ultrices gravida. Risus commodo viverra maecenas acc umsan lacus vel facilisis.</p>

  <div class="row-title" style="left:61px;top:754px;width:80px">TEACHING AND TRAINING</div>
  <div class="row-sub" style="left:61px;top:787px;width:110px">Utilizing the potential of hybrid learning</div>
  <p class="row-copy" style="left:61px;top:813px;width:118px">Lorem ipsum dolor sit amet, consectetur adipiscing elit, sed do eiusmod tempor incididunt ut labore et dolore magna aliqu auis ipsum suspendisse ultrices gravida. Risus commodo viverra maecenas acc umsan lacus vel facilisis.</p>
  <div class="art" style="left:190px;top:755px;width:212px;height:122px;background:linear-gradient(135deg,#eef4fb,#93bdef 55%,#2f3a7f)" role="img" aria-label="Illustration of a presenter at a whiteboard and a person working on a laptop"></div>

  <!-- about -->
  <div class="about"></div>
  <svg class="abs" style="left:0;top:925px" width="426" height="30" viewBox="0 0 426 30">
    <path d="M0,0 H426 V4 C300,-2 160,6 0,28 Z" fill="#ffffff"/>
  </svg>
  <svg class="abs" style="left:0;top:1140px" width="426" height="36" viewBox="0 0 426 36">
    <path d="M0,22 C120,34 300,30 426,8 V36 H0 Z" fill="#ffffff"/>
    <path d="M0,22 C120,34 300,30 426,8" fill="none" stroke="#8fd0f7" stroke-width="3" opacity=".7"/>
  </svg>
  <h2 class="h-section" style="left:50px;top:980px;color:#fff;font-size:18px">About Us</h2>
  <p class="about-copy">Within our pilot project "Open Pathways for Peace Learning" the Northbridge University (NBU) in cooperation with the Eastvale National Academy (ENA) uses means of digitalization to develop and teach up-to-date skills in conflict analysis and conflict transformation. These efforts are supported by the Academic Exchange Council (AEC) within the program "Bridges for Learning: partner university exchange grants"</p>
  <div class="art" style="left:206px;top:975px;width:177px;height:158px;background:linear-gradient(135deg,#5ab8f5,#e8f2fb 45%,#2b6fd6)" role="img" aria-label="Isometric illustration of a laptop, books, a clock and a small person studying"></div>

  <!-- videos -->
  <h2 class="h-section center" style="top:1209px;font-size:21px;font-weight:600">Our Videos</h2>
  <div class="art" style="left:37px;top:1250px;width:167px;height:122px;border-radius:0;background:linear-gradient(180deg,#5fb1f0,#7fb6ef 45%,#2c3f9f 80%,#1c2070)" role="img" aria-label="Video still: a woman using a phone on a mountain hillside"></div>
  <div class="art" style="left:210px;top:1250px;width:166px;height:122px;border-radius:0;background:linear-gradient(180deg,#6aa8ee,#b39be0 45%,#3a3aa6 75%,#1c1f6e)" role="img" aria-label="Video still: a person relaxing in a deck chair with a laptop on a hilltop"></div>
  <div class="play" style="left:106px;top:1297px;width:30px;height:30px"><svg width="12" height="14" viewBox="0 0 12 14"><path d="M2,1 L11,7 L2,13 Z" fill="#fff"/></svg></div>
  <div class="play" style="left:278px;top:1297px;width:30px;height:30px"><svg width="12" height="14" viewBox="0 0 12 14"><path d="M2,1 L11,7 L2,13 Z" fill="#fff"/></svg></div>

  <!-- blog -->
  <div class="blog-band"></div>
  <h2 class="h-section center" style="top:1450px;font-size:19px;font-weight:600">Latest Blog</h2>
  <div class="art" style="left:61px;top:1488px;width:131px;height:84px;border-radius:0;background:linear-gradient(135deg,#2fc0f2,#1b8ee6 60%,#1c3f9a)" role="img" aria-label="Illustration of people working with a large laptop and charts"></div>
  <div class="art" style="left:203px;top:1488px;width:75px;height:65px;border-radius:0;background:linear-gradient(135deg,#bfe3fb,#3e9ae9 70%)" role="img" aria-label="Illustration of a laptop with a clock and a small person"></div>
  <div class="art" style="left:290px;top:1488px;width:75px;height:65px;border-radius:0;background:linear-gradient(135deg,#efd0ef,#9aa2ee 60%,#6f4fd6)" role="img" aria-label="Illustration of an online study laptop with books and a lamp"></div>

  <div class="blog-title" style="left:61px;top:1580px;width:130px">Lorem ipsum dolor sit ameonsect etur adipiscing elitagna aliua.</div>
  <div class="blog-date" style="left:61px;top:1600px">November 2, 2021</div>
  <p class="blog-copy" style="left:61px;top:1609px;width:118px">Lorem ipsum dolor sit amet, consectetur adipisci elit, sed do eiusmod tempor inc ididunt ut labore et dolore magna aliqua. Quis ipsum suspendisse ultr ices gravida. Risus commodo viverra mae</p>
  <div class="blog-title" style="left:203px;top:1558px;width:76px">Lorem ipsum dolor sit amet consect</div>
  <div class="blog-date" style="left:203px;top:1577px">November 2, 2021</div>
  <p class="blog-copy" style="left:203px;top:1587px;width:75px">Lorem ipsum dolor sit am et, consectetur adipiscing elit,ed do eiusmod lotem por incididunt ut lab ore et dolore magnloa aliqua. Quis ipsum suspends se ultr ices gravida. Risus com mo do viverra</p>
  <div class="blog-title" style="left:290px;top:1558px;width:76px">Lorem ipsum dolor sit amet consect</div>
  <div class="blog-date" style="left:290px;top:1577px">November 2, 2021</div>
  <p class="blog-copy" style="left:290px;top:1587px;width:75px">Lorem ipsum dolor sit am et, consectetur adipiscing elit,ed do eiusmod lotem por incididunt ut lab ore et dolore magnloa aliqua. Quis ipsum suspends se ultr ices gravida. Risus com mo do viverra</p>

  <!-- contact navy -->
  <svg class="abs" style="left:0;top:1700px" width="426" height="48" viewBox="0 0 426 48">
    <path d="M0,20 C100,50 280,52 426,0 V48 H0 Z" fill="#1b1f6b"/>
    <path d="M0,20 C100,50 280,52 426,0" fill="none" stroke="#1a8fe3" stroke-width="4"/>
  </svg>
  <div class="contact-navy"></div>
  <h2 class="h-section center" style="top:1785px;color:#fff;font-size:17px;font-weight:600">CONTACT US</h2>
  <div class="contact-item" style="left:104px;top:1821px">
    <span class="icon-round"><svg width="9" height="9" viewBox="0 0 24 24"><path d="M6.6 10.8c1.4 2.8 3.8 5.1 6.6 6.6l2.2-2.2c.3-.3.7-.4 1-.2 1.1.4 2.3.6 3.6.6.6 0 1 .4 1 1V20c0 .6-.4 1-1 1C10.6 21 3 13.4 3 4c0-.6.4-1 1-1h3.5c.6 0 1 .4 1 1 0 1.3.2 2.5.6 3.6.1.3 0 .7-.2 1L6.6 10.8z" fill="#fff"/></svg></span>Phone:(555) 010 2240
  </div>
  <div class="contact-item" style="left:210px;top:1821px">
    <span class="icon-round"><svg width="9" height="9" viewBox="0 0 24 24"><rect x="2" y="5" width="20" height="14" rx="2" fill="#fff"/><path d="M3,6 L12,13 L21,6" fill="none" stroke="#1a8fe3" stroke-width="2"/></svg></span>hello@northbridge-uni.example
  </div>
  <div class="field" style="left:87px;top:1854px;width:124px;height:15px">Your Name</div>
  <div class="field" style="left:87px;top:1874px;width:124px;height:15px">Email Address</div>
  <div class="field" style="left:87px;top:1894px;width:124px;height:16px">Phone</div>
  <div class="field" style="left:215px;top:1854px;width:124px;height:56px">Message</div>
  <div class="btn" style="left:168px;top:1925px;width:65px;height:19px">SUBMIT</div>

  <footer class="footer-light">
    <div class="brand" style="left:165px;top:8px"><span class="brand-dot"></span>Harmony Learning</div>
    <div class="line" style="top:38px;font-weight:600">Cross-Border Cooperation</div>
    <div class="line" style="top:51px">NORTHBRIDGE UNIVERSITY</div>
    <div class="line" style="top:59px">EASTVALE NATIONAL ACADEMY</div>
    <div class="line" style="top:78px">© 2021All Rights Reserved. Privacy Policy &nbsp;|&nbsp; Sitemap</div>
  </footer>
</section>

</body>
</html>
```